Artwork-Design (Cover) für Musikalbum
Zielgruppe
Wir sind eine Tonträgerfirma und bewegen uns im Low-Budget-Segment.
Aufgabenstellung
Artwork-Design (Cover) für ein Musikalbum : 'Songs From The Prairie'
Wir benötigen nicht das komplette Artwork, sondern ein Frontcover
(121 x 120 mm + 20 mm Beschnitt) wg. etwaiger Verschiebung der Positionierung.
Fertigstellung (Aufziehen des Inlays und Labels) erfolgt später bei uns im Hause.
Wir benötigen später eine offene psd-Datei mit allen Ebenen.
Wichtig: Schriften nicht gerastert ggfs. Schrift mitliefern.
Was wir uns vorstellen:
- Entsprechend der Musik Bild, Tracks Beispiele:
-HALF A MOONLIGHT - TALWIND
-FARMYARD LADY IN A GREY MOOD - MERRIT, ODESSA P
-MAGGIE PLEASE COME BACK TO THE HOLLOW - BAXLEY, ORVAL
-PORTRAIT OF A DRIFTER - HOLTZ, WADE
- Bildmaterial sollte bei bildwerkpool, lumarchiv oder p-depot ausgesucht werden, das Bildmaterial wird dann später auch von uns dort eingekauft.
- keine Künstlerfotos.
Wir freuen uns und sind sehr gespannt auf eure Vorschläge,
bei Fragen gerne mailen

```html
<!DOCTYPE html>
<html lang="en">
<head>
<meta charset="utf-8">
<title>Songs From The Prairie – Album Cover</title>
<link rel="stylesheet" href="https://fonts.googleapis.com/css2?family=Smokum&family=Oranienbaum&display=swap">
<style>
  :root {
    --stage: #3b3b3b;
    --paper: #f8f0e4;
    --ink: #5a3216;
    --line: #7a5a44;
    --blue: #2f9be8;
    --blue-soft: #8cc6f0;
    --orange: #f3781b;
  }
  html, body {
    margin: 0;
    padding: 0;
    width: 1200px;
    height: 2400px;
    overflow: hidden;
    background: var(--stage);
  }
  .canvas {
    position: relative;
    width: 1200px;
    height: 2400px;
  }
  .cover {
    position: absolute;
    left: 120px;
    top: 720px;
    width: 960px;
    height: 960px;
    background: var(--paper);
    overflow: hidden;
  }
  .artwork {
    position: absolute;
    inset: 0;
    background:
      radial-gradient(ellipse 70px 150px at 30px 330px, rgba(243,120,27,0.95), rgba(243,120,27,0) 100%),
      radial-gradient(ellipse 260px 170px at 430px 400px, rgba(47,155,232,0.9), rgba(47,155,232,0) 100%),
      radial-gradient(ellipse 230px 260px at 800px 650px, rgba(47,155,232,0.95), rgba(47,155,232,0) 100%),
      radial-gradient(ellipse 200px 190px at 610px 460px, rgba(47,155,232,0.85), rgba(47,155,232,0) 100%),
      radial-gradient(ellipse 160px 300px at 900px 300px, rgba(140,198,240,0.7), rgba(140,198,240,0) 100%),
      radial-gradient(ellipse 150px 120px at 760px 880px, rgba(47,155,232,0.6), rgba(47,155,232,0) 100%);
  }
  .frame {
    position: absolute;
    inset: 0;
  }
  .artist {
    position: absolute;
    top: 52px;
    left: 0;
    width: 960px;
    text-align: center;
    margin: 0;
    font-family: "Smokum", serif;
    font-weight: 400;
    font-size: 38px;
    color: var(--ink);
  }
  .title {
    position: absolute;
    left: 118px;
    top: 540px;
    margin: 0;
    font-family: "Smokum", serif;
    font-weight: 400;
    font-size: 112px;
    line-height: 124px;
    color: var(--ink);
  }
  .title span { display: block; }
  .tagline {
    position: absolute;
    left: 132px;
    top: 818px;
    margin: 0;
    font-family: "Oranienbaum", serif;
    font-size: 26px;
    color: var(--ink);
  }
</style>
</head>
<body>
<main class="canvas">
  <section class="cover">
    <div class="artwork" role="img" aria-label="Blue watercolour illustration of hands playing an acoustic guitar neck, with an orange paint splash at the left edge"></div>
    <svg class="frame" width="960" height="960" viewBox="0 0 960 960" aria-hidden="true">
      <g fill="none" stroke="var(--line)" stroke-width="2">
        <path d="M292 70 H79 V884 H889 V70 H674"/>
        <path d="M292 78 H88 V875 H880 V78 H674"/>
      </g>
    </svg>
    <p class="artist">John Doe &amp; Friends</p>
    <h1 class="title"><span>Songs From</span><span>The Prairie</span></h1>
    <p class="tagline">Lorem ipsum dolor sit amet, consectetur adipiscing elit.</p>
  </section>
</main>
</body>
</html>
```